BRIGHTHOLM ADVISORY powerpoint deck.

I REQUIRE A COMPANY POWERPOINT SLIDE DECK, WHICH MAY ALSO INCLUDE A NUMBER OF "MODELS". THIS MAY ALSO REQUIRE SOME FOLLOW UP WORK.

ATTACHED IS AN EXAMPLE SLIDE DECK FOR ONE OF MY CLIENTS. I would like to see a mock up of a few slides and then i can send a complete deck over.

Please note my website... www.brightholmadvisory.co.uk

I LOOK FORWARD TO SEEING YOUR DESIGN.

THANK YOU,

DAVID.

I work in the "learning and development"/ education/ leadership/ coaching industry

Leadership

Other font styles liked:
• century gothic

• ideally there would be some alignment to my website. www.brightholmadvisory.co.uk
• be fresh, clean, simple enough. look professional.
• how you present "models" i would come back for more work in the future if the work is good.
• too brash.

```html
<!DOCTYPE html>
<html lang="en">
<head>
<meta charset="utf-8">
<title>Brightholm Advisory – Presentation Deck</title>
<link href="https://fonts.googleapis.com/css2?family=Raleway:wght@300;400;600;700&display=swap" rel="stylesheet">
<style>
:root{
  --teal:#6cbcb4;
  --ink:#1f1f1f;
  --black:#000;
  --charcoal:#3a3a3a;
  --panel:#444;
  --grey:#8a8a8a;
  --muted:#a9a9a9;
  --white:#fff;
  --page:#f3f3f3;
}
*{box-sizing:border-box;margin:0;padding:0}
html,body{width:1200px;height:1189px;overflow:hidden;background:var(--page);font-family:'Raleway',sans-serif;color:var(--ink)}
.deck{display:grid;grid-template-columns:repeat(3,393px);grid-auto-rows:220px;column-gap:7px;row-gap:17px;padding:8px 0 0 3px}
.slide{position:relative;overflow:hidden;background:var(--white);box-shadow:0 1px 4px rgba(0,0,0,.18)}
.abs{position:absolute}
.photo{position:absolute}
.ph-dark{background:linear-gradient(135deg,#2a2a2a,#5a5a5a 55%,#1c1c1c)}
.ph-mid{background:linear-gradient(160deg,#8d8d8d,#cfcfcf 50%,#6e6e6e)}
.ph-warm{background:radial-gradient(circle at 50% 45%,#a2783c,#3a2a18 45%,#111 80%)}
.ph-sea{background:linear-gradient(180deg,#8a8a8a,#cfcfcf 55%,#5d5d5d)}
.ph-sky{background:linear-gradient(170deg,#d6d6d6,#7d7d7d 50%,#2d2d2d)}

.title{position:absolute;left:17px;top:16px;font-size:17px;font-weight:400;color:var(--ink)}
.title::after{content:"";position:absolute;left:0;bottom:-4px;width:28px;height:2px;background:var(--teal)}
.brand{position:absolute;display:flex;align-items:center;gap:3px;font-size:5px;font-weight:600;letter-spacing:.6px;color:var(--ink)}
.brand i{display:block;width:9px;height:9px;border-radius:50%;background:var(--teal)}
.brand.top{right:14px;top:12px}
.footer{position:absolute;left:0;right:0;bottom:0;height:11px;background:var(--black);color:var(--white);font-size:4px;line-height:11px;padding-left:4px}
.footer::after{content:"";position:absolute;right:0;top:0;width:12px;height:11px;background:var(--teal)}
.footer b{position:absolute;right:18px;font-weight:400;color:var(--muted)}
.tiny{font-size:4.5px;line-height:1.4;color:var(--muted);font-weight:400}
.lbl{font-size:7px;color:var(--ink)}
.white{color:var(--white)}

/* cover */
.cover .brand{left:0;right:0;top:132px;justify-content:center;font-size:21px;font-weight:300;letter-spacing:4px;color:var(--white);gap:8px}
.cover .brand i{width:22px;height:22px}

/* title slide */
.hero-band{position:absolute;left:0;right:0;top:155px;height:41px;background:rgba(0,0,0,.72);text-align:center;color:var(--white)}
.hero-band h1{font-size:17px;font-weight:300;margin-top:7px}
.hero-band p{font-size:5px}
.presenters{position:absolute;left:6px;right:8px;bottom:4px;display:flex;gap:18px;font-size:5px;color:var(--ink);align-items:center}
.presenters span.d{margin-left:auto;color:var(--grey)}

/* quote */
.quote-mark{position:absolute;left:178px;top:52px;width:36px;height:36px;border-radius:50%;background:var(--teal);color:var(--white);font-size:28px;font-weight:700;text-align:center;line-height:44px}
.quote-text{position:absolute;left:0;right:0;top:100px;text-align:center;color:#ddd;font-size:12px;font-weight:300;line-height:1.3}
.quote-text small{display:block;font-size:5.5px;margin-top:10px}

/* agenda */
.agenda-item{position:absolute;width:150px}
.agenda-item .ico{position:absolute;left:0;top:1px;width:13px;height:13px;background:var(--ink)}
.agenda-item .ico::after{content:"";position:absolute;left:3.5px;top:3.5px;width:6px;height:6px;border:1px solid var(--white);border-radius:50%}
.agenda-item .txt{margin-left:23px}
.agenda-item .time{font-size:4px;color:var(--teal)}

/* about */
.about-panel{position:absolute;left:195px;top:47px;width:198px;height:124px;background:rgba(60,60,60,.92);padding:20px 20px 0 20px;color:var(--white)}
.about-panel h2{font-size:17px;font-weight:400;margin-bottom:10px}
.about-panel p{font-size:5px;line-height:1.4;margin-bottom:5px;color:#e5e5e5}

/* services */
.svc{position:absolute;left:215px;width:160px}
.svc .dot{position:absolute;left:0;top:0;width:16px;height:16px;border-radius:50%;background:var(--ink)}
.svc .dot::after{content:"";position:absolute;left:5px;top:5px;width:6px;height:6px;border-radius:50%;background:var(--white)}
.svc .txt{margin-left:29px}

/* clients */
.client{position:absolute;width:98px;text-align:center;font-size:14px;font-weight:700;color:var(--ink)}
.client.sm{font-size:11px}
.client-box{position:absolute;left:99px;top:75px;width:197px;height:70px;background:var(--black);color:var(--white);font-size:18px;font-weight:300;text-align:center;line-height:70px}

/* text area */
.lead{font-size:8.5px;line-height:1.3;color:var(--ink)}
.body p{font-size:5.5px;line-height:1.45;color:var(--grey);margin-bottom:6px}

/* vision */
.vm-panel{position:absolute;left:0;right:0;top:50px;height:125px;background:linear-gradient(180deg,#3d3d3d,#4a4a4a)}
.vm-h{font-size:12px;font-weight:300;color:var(--white)}
.vm-row{position:absolute;left:227px;width:160px}
.vm-row .c{position:absolute;left:0;top:0;width:20px;height:20px;border-radius:50%;background:#ddd;border:3px solid #777}

/* text area framed */
.frame-card{position:absolute;left:14px;top:13px;width:365px;height:195px;background:var(--white);padding:0 15px}

/* swot */
.swot-lbl{position:absolute;font-size:10px;font-weight:400}

/* numbered */
.num{position:absolute;left:0;top:0;width:12px;height:12px;border-radius:50%;background:var(--black);color:var(--white);font-size:5px;text-align:center;line-height:12px}

/* tiles */
.tile{position:absolute;width:110px;height:64px;padding:8px 9px}
.tile h4{font-size:7px;font-weight:400;margin-bottom:5px}
.tile p{font-size:4.2px;line-height:1.35}

/* stairs */
.side-panel{position:absolute;left:196px;top:0;width:197px;height:220px;background:var(--black);color:var(--white);padding:20px 16px 0 16px}
.side-panel h3{font-size:9px;font-weight:700;line-height:1.25;width:120px;margin-bottom:10px}
.side-item{position:relative;padding-left:22px;margin-bottom:9px}
.side-item svg{position:absolute;left:0;top:0}
.side-item .l{font-size:6.5px}
.side-item .tiny{color:#cfcfcf}
</style>
</head>
<body>
<main class="deck">

  <!-- 1 Cover -->
  <section class="slide cover">
    <div class="photo ph-dark" style="inset:0" role="img" aria-label="Black and white spiral staircase seen from above"></div>
    <div class="brand"><i></i>BRIGHTHOLM</div>
  </section>

  <!-- 2 Title -->
  <section class="slide">
    <div class="photo ph-mid" style="left:0;top:0;width:393px;height:200px" role="img" aria-label="Group of smiling business people in suits"></div>
    <svg class="abs" style="left:0;top:0" width="393" height="75" viewBox="0 0 393 75"><path d="M0 0H393V22C330 22 275 26 245 50C228 64 212 68 190 68H0Z" fill="#fff"/></svg>
    <div class="brand" style="left:45px;top:22px"><i></i>BRIGHTHOLM</div>
    <div class="hero-band"><h1>Your Title Goes Here</h1><p>Your Subtitle Goes Here</p></div>
    <div class="presenters"><span>John Smith</span><span>Jane Smith</span><span>Jack Brown</span><span class="d">Cityname | November 28, 2017</span></div>
  </section>

  <!-- 3 Quote -->
  <section class="slide">
    <div class="photo ph-dark" style="inset:0;background:linear-gradient(120deg,#1c1c1c,#3a3a3a 60%,#222)" role="img" aria-label="Row of light bulbs in the dark"></div>
    <div class="quote-mark">“</div>
    <div class="quote-text">Coming together is a beginning.<br>Keeping together is progress.<br>Working together is success.<small>- Harold Fenwick -</small></div>
  </section>

  <!-- 4 Agenda -->
  <section class="slide">
    <div class="title">Our Agenda</div>
    <div class="brand top"><i></i>BRIGHTHOLM</div>
    <div class="agenda-item" style="left:56px;top:62px"><div class="ico"></div><div class="txt"><div class="lbl">Agenda One</div><div class="time">10:00</div><div class="tiny">Lorem ipsum dolor sit amet, consectetur adipiscing elit, sed do eiusmod.</div></div></div>
    <div class="agenda-item" style="left:56px;top:108px"><div class="ico"></div><div class="txt"><div class="lbl">Agenda Two</div><div class="time">11:00</div><div class="tiny">Lorem ipsum dolor sit amet, consectetur adipiscing elit, sed do eiusmod.</div></div></div>
    <div class="agenda-item" style="left:56px;top:153px"><div class="ico"></div><div class="txt"><div class="lbl">Agenda Three</div><div class="time">12:00</div><div class="tiny">Lorem ipsum dolor sit amet, consectetur adipiscing elit, sed do eiusmod.</div></div></div>
    <div class="agenda-item" style="left:215px;top:62px"><div class="ico"></div><div class="txt"><div class="lbl">Agenda Four</div><div class="time">13:00</div><div class="tiny">Lorem ipsum dolor sit amet, consectetur adipiscing elit, sed do eiusmod.</div></div></div>
    <div class="agenda-item" style="left:215px;top:108px"><div class="ico"></div><div class="txt"><div class="lbl">Agenda Five</div><div class="time">14:00</div><div class="tiny">Lorem ipsum dolor sit amet, consectetur adipiscing elit, sed do eiusmod.</div></div></div>
    <div class="agenda-item" style="left:215px;top:153px"><div class="ico"></div><div class="txt"><div class="lbl">Agenda Six</div><div class="time">15:00</div><div class="tiny">Lorem ipsum dolor sit amet, consectetur adipiscing elit, sed do eiusmod.</div></div></div>
    <div class="footer">© 2017 BRIGHTHOLM Advisory All rights reserved<b>4</b></div>
  </section>

  <!-- 5 About -->
  <section class="slide">
    <div class="photo ph-sky" style="inset:0" role="img" aria-label="Business team in suits standing together"></div>
    <div class="brand top" style="color:var(--white)"><i></i>BRIGHTHOLM</div>
    <div class="about-panel"><h2>About Us</h2><p>Lorem ipsum dolor sit amet, consectetur adipiscing elit, sed do eiusmod tempor incididunt ut labore et dolore magna aliqua.</p><p>Ut enim ad minim veniam, quis nostrud exercitation ullamco laboris nisi ut aliquip ex ea commodo consequat.</p></div>
    <div class="footer">© 2017 BRIGHTHOLM Advisory All rights reserved<b>5</b></div>
  </section>

  <!-- 6 Services -->
  <section class="slide">
    <div class="title">Our Services</div>
    <div class="brand top"><i></i>BRIGHTHOLM</div>
    <div class="photo ph-warm" style="left:36px;top:51px;width:153px;height:96px" role="img" aria-label="Glowing vintage light bulbs"></div>
    <div class="abs" style="left:36px;top:155px;width:153px"><div class="lbl">Your Title Goes Here</div><div class="tiny">Lorem ipsum adipiscing elit, sed do eiusmod tempor incididunt ut labore et dolore magna aliqua. Ut enim minim veniam, quis nostrud exercitation ullamco laboris.</div></div>
    <div class="svc" style="top:52px"><div class="dot"></div><div class="txt"><div class="lbl">Service Number One</div><div class="tiny">Lorem ipsum dolor sit amet, consectetur adipiscing elit, sed do eiusmod tempor incididunt ut labore.</div></div></div>
    <div class="svc" style="top:99px"><div class="dot"></div><div class="txt"><div class="lbl">Service Number Two</div><div class="tiny">Lorem ipsum dolor sit amet, consectetur adipiscing elit, sed do eiusmod tempor incididunt ut labore.</div></div></div>
    <div class="svc" style="top:146px"><div class="dot"></div><div class="txt"><div class="lbl">Service Number Three</div><div class="tiny">Lorem ipsum dolor sit amet, consectetur adipiscing elit, sed do eiusmod tempor incididunt ut labore.</div></div></div>
    <div class="footer">© 2017 BRIGHTHOLM Advisory All rights reserved<b>6</b></div>
  </section>

  <!-- 7 Quote Area -->
  <section class="slide">
    <div class="title">Quote Area</div>
    <div class="brand top"><i></i>BRIGHTHOLM</div>
    <div class="abs" style="left:0;top:47px;width:196px;height:136px;background:var(--charcoal)"></div>
    <div class="photo ph-sea" style="left:196px;top:47px;width:197px;height:136px" role="img" aria-label="Sailing dinghies racing on grey water"></div>
    <div class="abs white" style="left:32px;top:88px;font-size:10px;font-weight:300;line-height:1.2">Coming together is a beginning.<br>Keeping together is progress.<br>Working together is success.<div style="font-size:6px;margin-top:8px;color:#bbb">- Harold Fenwick -</div></div>
    <div class="footer">© 2017 BRIGHTHOLM Advisory All rights reserved<b>7</b></div>
  </section>

  <!-- 8 Clients -->
  <section class="slide">
    <div class="client sm" style="left:0;top:30px">Northfield Hockey</div>
    <div class="client" style="left:99px;top:33px">Velocar</div>
    <div class="client" style="left:197px;top:33px">Aldmere</div>
    <div class="client" style="left:295px;top:33px">Korran</div>
    <div class="client sm" style="left:0;top:103px">Halvern Bank</div>
    <div class="client-box">The Client</div>
    <div class="client sm" style="left:295px;top:103px">Tri Union</div>
    <div class="client" style="left:0;top:172px">Vistel</div>
    <div class="client sm" style="left:99px;top:168px">Stride Athletics</div>
    <div class="client sm" style="left:197px;top:168px">Stoneway Land</div>
    <div class="client sm" style="left:295px;top:168px">Aqua League</div>
  </section>

  <!-- 9 Text Area -->
  <section class="slide">
    <div class="title">Text Area</div>
    <div class="brand top"><i></i>BRIGHTHOLM</div>
    <div class="abs" style="left:33px;top:63px;width:330px">
      <p class="lead">This is place for your header text. Insert your text here, just replace this text with your own text</p>
      <div class="body" style="margin-top:9px">
        <p>Lorem ipsum dolor sit amet, consectetur adipiscing elit, sed do eiusmod tempor incididunt ut labore et dolore magna aliqua. Ut enim ad minim veniam, quis nostrud exercitation ullamco laboris nisi ut aliquip ex ea commodo consequat.</p>
        <p>Duis aute irure dolor in reprehenderit in voluptate velit esse cillum dolore eu fugiat nulla pariatur. Excepteur sint occaecat cupidatat non proident, sunt in culpa qui officia deserunt mollit anim id est laborum.</p>
        <p>Ut enim ad minim veniam, quis nostrud exercitation ullamco laboris nisi ut aliquip ex ea commodo consequat.</p>
      </div>
    </div>
    <div class="footer">© 2017 BRIGHTHOLM Advisory All rights reserved<b>9</b></div>
  </section>

  <!-- 10 Vision & Mission -->
  <section class="slide">
    <div class="title">Our Vision &amp; Mission</div>
    <div class="brand top"><i></i>BRIGHTHOLM</div>
    <div class="vm-panel" role="img" aria-label="Dark brick wall with hanging lamps"></div>
    <div class="abs" style="left:22px;top:72px;width:165px">
      <div class="vm-h">Our Vision:</div>
      <div class="white" style="font-size:9px;font-weight:700;line-height:1.3">Go to the Next Level<br>Without look in the past</div>
      <div style="width:22px;height:2px;background:var(--teal);margin:5px 0 7px"></div>
      <div class="tiny" style="color:#ddd">Lorem ipsum dolor sit amet, consectetur adipiscing elit, sed do eiusmod tempor incididunt ut labore et dolore magna aliqua. Ut enim minim veniam, quis nostrud exercitation ullamco laboris nisi ut aliquip ex ea commodo consequat.</div>
    </div>
    <div class="abs vm-h" style="left:222px;top:72px">Our Missions:</div>
    <div class="vm-row" style="top:90px"><div class="c"></div><div style="margin-left:30px"><div class="white" style="font-size:6.5px">Your Text Here</div><div class="tiny" style="color:#ddd">Lorem ipsum dolor sit consectetur adipiscing elit, sed do eiusmod tempo.</div></div></div>
    <div class="vm-row" style="top:121px"><div class="c"></div><div style="margin-left:30px"><div class="white" style="font-size:6.5px">Your Text Here</div><div class="tiny" style="color:#ddd">Lorem ipsum dolor sit consectetur adipiscing elit, sed do eiusmod tempo.</div></div></div>
    <div class="vm-row" style="top:152px"><div class="c"></div><div style="margin-left:30px"><div class="white" style="font-size:6.5px">Your Text Here</div><div class="tiny" style="color:#ddd">Lorem ipsum dolor sit consectetur adipiscing elit, sed do eiusmod tempo.</div></div></div>
    <div class="footer">© 2017 BRIGHTHOLM Advisory All rights reserved<b>10</b></div>
  </section>

  <!-- 11 Text Area framed -->
  <section class="slide" style="background:linear-gradient(90deg,var(--black) 49%,var(--teal) 49%)">
    <div class="frame-card">
      <div class="title" style="left:20px;top:28px">Text Area</div>
      <div class="brand" style="right:16px;top:28px"><i></i>BRIGHTHOLM</div>
      <div class="abs" style="left:20px;top:76px;width:325px">
        <p class="lead">This is place for your header text. Insert your text here, just replace this text with your own text</p>
        <div class="body" style="margin-top:9px">
          <p>Lorem ipsum dolor sit amet, consectetur adipiscing elit, sed do eiusmod tempor incididunt ut labore et dolore magna aliqua. Ut enim ad minim veniam, quis nostrud exercitation ullamco laboris commodo consequat.</p>
          <p>Duis aute irure dolor in reprehenderit in voluptate velit esse cillum dolore eu fugiat nulla pariatur. Excepteur sint occaecat cupidatat non proident, sunt in culpa qui officia deserunt mollit anim id est laborum.</p>
          <p>Ut enim minim veniam, quis nostrud exercitation ullamco laboris nisi ut aliquip ex ea commodo consequat. Lorem ipsum dolor sit amet, consectetur adipiscing elit, sed do eiusmod tempor.</p>
        </div>
      </div>
    </div>
  </section>

  <!-- 12 SWOT -->
  <section class="slide">
    <div class="title">SWOT Analysis</div>
    <div class="brand top"><i></i>BRIGHTHOLM</div>
    <svg class="abs" style="left:0;top:0" width="393" height="220" viewBox="0 0 393 220">
      <rect x="184" y="66" width="24" height="104" rx="12" fill="#1f1f1f"/>
      <rect x="142" y="104" width="108" height="24" rx="12" fill="#6cbcb4"/>
      <rect x="184" y="104" width="24" height="24" fill="#1f1f1f"/>
      <circle cx="196" cy="116" r="7" fill="#fff"/>
      <circle cx="196" cy="77" r="7" fill="#fff"/><circle cx="196" cy="77" r="2.5" fill="#1f1f1f"/>
      <circle cx="153" cy="116" r="7" fill="#fff"/><circle cx="153" cy="116" r="2.5" fill="#6cbcb4"/>
      <circle cx="239" cy="116" r="7" fill="#fff"/><path d="M236 117l6-3-2 6z" fill="#6cbcb4"/>
      <circle cx="196" cy="159" r="7" fill="#6cbcb4"/><rect x="193" y="156" width="6" height="6" fill="#fff"/>
      <text x="190" y="101" font-family="Raleway" font-size="8" fill="#fff">O</text>
      <text x="203" y="123" font-family="Raleway" font-size="8" fill="#1f1f1f">T</text>
      <text x="167" y="123" font-family="Raleway" font-size="8" fill="#1f1f1f">W</text>
      <text x="191" y="144" font-family="Raleway" font-size="8" fill="#fff">S</text>
    </svg>
    <div class="swot-lbl" style="left:236px;top:62px">• Strengths<div class="tiny" style="width:70px;font-size:3.5px">Lorem ipsum dolor sit amet, dolor sunt ut consequat lorem.</div></div>
    <div class="swot-lbl" style="left:80px;top:88px;color:var(--teal);text-align:right">• Threats<div class="tiny" style="width:58px;font-size:3.5px">Lorem ipsum dolor sit amet, dolor sunt ut consequat.</div></div>
    <div class="swot-lbl" style="left:262px;top:122px;color:var(--teal)">• Weaknesses<div class="tiny" style="width:70px;font-size:3.5px">Lorem ipsum dolor sit amet, dolor sunt ut consequat.</div></div>
    <div class="swot-lbl" style="left:72px;top:150px">• Opportunities<div class="tiny" style="width:70px;font-size:3.5px;padding-left:16px">Lorem ipsum dolor sit amet, dolor sunt ut consequat.</div></div>
    <div class="footer">© 2017 BRIGHTHOLM Advisory All rights reserved<b>12</b></div>
  </section>

  <!-- 13 Numbered -->
  <section class="slide">
    <div class="photo ph-mid" style="left:0;top:0;width:196px;height:209px;background:linear-gradient(160deg,#f2f2f2,#bdbdbd 45%,#555 70%,#333)" role="img" aria-label="Hand using a tablet computer"></div>
    <div class="abs" style="left:0;top:111px;width:196px;height:98px;background:rgba(40,40,40,.75)"></div>
    <div class="brand" style="left:65px;top:153px;color:var(--white);font-size:7px"><i></i>BRIGHTHOLM</div>
    <div class="brand top"><i></i>BRIGHTHOLM</div>
    <div class="abs" style="left:215px;top:55px;font-size:15px;font-weight:400">Your Title Goes Here</div>
    <div class="abs" style="left:215px;top:86px;width:140px"><div class="num">1</div><div style="margin-left:23px"><div class="lbl">Your Text Goes Here</div><div class="tiny">Lorem ipsum dolor sit amet, consectetur adipiscing elit, sed do eiusmod tempor incididunt ut labore et dolore magna aliqua.</div></div></div>
    <div class="abs" style="left:215px;top:139px;width:140px"><div class="num">2</div><div style="margin-left:23px"><div class="lbl">Your Text Goes Here</div><div class="tiny">Lorem ipsum dolor sit amet, consectetur adipiscing elit, sed do eiusmod tempor incididunt ut labore et dolore magna aliqua.</div></div></div>
    <div class="footer">© 2017 BRIGHTHOLM Advisory All rights reserved<b>13</b></div>
  </section>

  <!-- 14 Tiles -->
  <section class="slide">
    <div class="title">Your Title Goes Here</div>
    <div class="brand top"><i></i>BRIGHTHOLM</div>
    <div class="photo ph-sky" style="left:28px;top:57px;width:110px;height:64px" role="img" aria-label="Business team portrait"></div>
    <div class="tile white" style="left:141px;top:57px;background:var(--teal)"><h4>Heading Goes Here</h4><p>Lorem ipsum dolor sit amet, consectetur adipiscing elit, sed do eiusmod tempor incididunt ut labore et commodo.</p></div>
    <div class="photo ph-mid" style="left:254px;top:57px;width:110px;height:64px" role="img" aria-label="Smiling businessmen"></div>
    <div class="tile white" style="left:28px;top:124px;background:var(--black)"><h4>Heading Goes Here</h4><p>Lorem ipsum dolor sit amet, consectetur adipiscing elit, sed do eiusmod tempor incididunt ut labore et commodo.</p></div>
    <div class="photo" style="left:141px;top:124px;width:110px;height:64px;background:linear-gradient(180deg,#111,#3a3a3a 60%,#bbb)" role="img" aria-label="Chess pieces on a board"></div>
    <div class="tile white" style="left:254px;top:124px;background:var(--grey)"><h4>Heading Goes Here</h4><p>Lorem ipsum dolor sit amet, consectetur adipiscing elit, sed do eiusmod tempor incididunt ut labore et commodo.</p></div>
    <div class="footer">© 2017 BRIGHTHOLM Advisory All rights reserved<b>14</b></div>
  </section>

  <!-- 15 Side panel -->
  <section class="slide">
    <div class="photo ph-sky" style="left:0;top:0;width:196px;height:220px" role="img" aria-label="Concrete staircase rising toward a cloudy sky"></div>
    <div class="side-panel">
      <div class="brand" style="right:10px;top:14px;color:var(--white)"><i></i>BRIGHTHOLM</div>
      <h3>This is place for your header text. Insert your text here, just replace this text with your own text</h3>
      <div class="side-item"><svg width="12" height="12" viewBox="0 0 12 12"><circle cx="5" cy="5" r="3.5" fill="none" stroke="#fff" stroke-width="1.5"/><path d="M7.5 7.5L11 11" stroke="#fff" stroke-width="1.8"/></svg><div class="l">Your Text Here</div><div class="tiny">Lorem ipsum dolor sit amet, consectetur adipiscing elit, sed do eiusmod.</div></div>
      <div class="side-item"><svg width="12" height="12" viewBox="0 0 12 12"><path d="M2 10L9 3l1.5 1.5-7 7H2z" fill="#fff"/></svg><div class="l">Your Text Here</div><div class="tiny">Lorem ipsum dolor sit amet, consectetur adipiscing elit, sed do eiusmod.</div></div>
      <div class="side-item"><svg width="12" height="12" viewBox="0 0 12 12"><path d="M11 1L4 6l2 2zM3 7l-2 4 4-2z" fill="#fff"/></svg><div class="l">Your Text Here</div><div class="tiny">Lorem ipsum dolor sit amet, consectetur adipiscing elit, sed do eiusmod.</div></div>
      <div class="side-item"><svg width="12" height="12" viewBox="0 0 12 12"><circle cx="6" cy="6" r="4" fill="none" stroke="#fff" stroke-width="2.4" stroke-dasharray="2 1.2"/><circle cx="6" cy="6" r="1.5" fill="#fff"/></svg><div class="l">Your Text Here</div><div class="tiny">Lorem ipsum dolor sit amet, consectetur adipiscing elit, sed do eiusmod.</div></div>
    </div>
  </section>

</main>
</body>
</html>
```